Email Marketing Campaign 50% discount and buy-2-get-1 offer

I would like to inform my customers of our special offers via a e-Newsletter/Marketing E-Mail.

The coding needs to be done by the designer.

I have most of the design and the message that we wish to convey our buyers.

The information is:

1. We have now 50% discount on all our carpets

2. We have a buy-2 get-1 free carpet offer

For both the above messages we have already banner style that we like to use in our Newsletter.
I have attached the banner and the designers can use it.

3. We have opened a new shop in Berlin Germany

Therefore we like to have a Sylish Newsletter design that fits our website and products using the banner idea and we wish to include the 3 messages.
Special note should be given that this newsletter is going to our previous buyers. Therefore they already know us, and we just like to inform them of our latest news and offer.

Target Market(s)

Upmarket buyers looking for a great deal

Industry/Entity Type

Marketing

Coding

Coded - Design and coding required

Number of Pages Required

1 page

Font styles to use
Sans Serif

Colors
e667a6
34a7d8

Requirements
Must have
• Clear explanation with excitement in the message
Nice to have
• To promote clearly the 3 for 2 with maybe an explanation and clear images describing what the promotion is and how it works.
• I.e. buy 2 get 1 extra carpet of your choice free
• Add carpets to checkout and the system will calculate automatically
• The lowest carpet in your selection of 3 is the free carpet

```html
<!DOCTYPE html>
<html lang="en">
<head>
<meta charset="utf-8">
<title>Loomhaus Rugs – Newsletter</title>
<link rel="stylesheet" href="https://fonts.googleapis.com/css2?family=Lato:wght@300;400;700;900&family=Open+Sans:wght@700;800&display=swap">
<style>
  :root {
    --white: #ffffff;
    --ink: #1a1a1a;
    --brand-grey: #7a7a7d;
    --ribbon-red: #d3202b;
    --band-dark: rgba(40, 38, 38, 0.62);
    --band-soft: rgba(45, 40, 40, 0.55);
    --button-bg: #e6e6e6;
    --button-text: #444444;
    --accent-pink: #e667a6;
    --accent-blue: #34a7d8;
  }
  * { margin: 0; padding: 0; box-sizing: border-box; }
  html, body { width: 1200px; height: 590px; overflow: hidden; background: var(--white); }
  body { position: relative; font-family: "Lato", Arial, sans-serif; }

  .brand {
    position: absolute; left: 0; width: 1200px; top: 44px;
    display: flex; justify-content: center; align-items: center; gap: 12px;
  }
  .brand-dot { width: 14px; height: 14px; border-radius: 50%; background: var(--brand-grey); }
  .brand-name {
    font-family: "Lato", Arial, sans-serif; font-weight: 300; font-size: 44px;
    color: var(--brand-grey); letter-spacing: 1px; line-height: 1;
  }

  .banner { position: absolute; overflow: hidden; }
  .banner-photo { position: absolute; inset: 0; }
  .ribbon { position: absolute; left: 0; top: 0; }

  /* main sale banner */
  .sale-banner { left: 48px; top: 127px; width: 726px; height: 399px; }
  .sale-banner .banner-photo {
    background: linear-gradient(180deg, #6f8a5d 0%, #a9b59b 22%, #e4e3df 45%, #dcd6cf 62%, #d9b9b4 78%, #cfc08e 100%);
  }
  .headline {
    position: absolute; color: var(--white); white-space: nowrap;
    font-family: "Open Sans", Arial, sans-serif; font-weight: 700; line-height: 1;
    text-shadow: 0 2px 6px rgba(0,0,0,0.25);
  }
  .headline-upto { left: 58px; top: 30px; font-size: 34px; letter-spacing: -0.5px; }
  .headline-fifty { left: 44px; top: 50px; font-size: 134px; letter-spacing: -8px; }
  .headline-percent { left: 188px; top: 58px; font-size: 86px; letter-spacing: -2px; }
  .headline-off { left: 189px; top: 136px; font-size: 38px; letter-spacing: -1.5px; }
  .headline-sale { left: 48px; top: 162px; font-size: 116px; letter-spacing: -4px; }
  .headline-nowon { left: 162px; top: 263px; font-size: 31px; letter-spacing: -0.5px; }
  .bracket { position: absolute; left: 0; top: 0; }

  .offer-band {
    position: absolute; left: 0; bottom: 0; width: 100%; height: 89px;
    background: var(--band-dark);
  }
  .offer-text {
    position: absolute; left: 41px; top: 18px; color: var(--white);
    font-size: 24px; line-height: 24px; font-weight: 400; text-transform: uppercase;
  }
  .shop-button {
    position: absolute; left: 581px; top: 18px; width: 113px; height: 48px;
    background: var(--button-bg); color: var(--button-text); border-radius: 3px;
    font-size: 14px; display: flex; align-items: center; justify-content: center;
  }

  /* side banners */
  .side-banner { left: 790px; width: 354px; }
  .promo-banner { top: 127px; height: 188px; }
  .promo-banner .banner-photo {
    background: linear-gradient(180deg, #3d3f48 0%, #7c7d86 30%, #a9a59e 55%, #b78a55 70%, #8f1e3a 85%, #a1254a 100%);
  }
  .store-banner { top: 335px; height: 188px; }
  .store-banner .banner-photo {
    background: linear-gradient(90deg, #7a9a58 0%, #c9cbc4 22%, #ebeae6 50%, #c8c4bd 78%, #879a6a 100%);
  }
  .store-banner .banner-photo::after {
    content: ""; position: absolute; left: 0; right: 0; bottom: 0; height: 70px;
    background: linear-gradient(180deg, rgba(40,42,60,0) 0%, #2b2e45 60%, #6b4a2d 100%);
  }
  .side-title {
    position: absolute; left: 0; width: 100%; text-align: center; color: var(--white);
    font-family: "Open Sans", Arial, sans-serif; font-weight: 800; line-height: 1;
    text-shadow: 0 2px 8px rgba(0,0,0,0.35);
  }
  .promo-title { top: 43px; font-size: 95px; letter-spacing: -4px; }
  .store-title { top: 3px; font-size: 76px; line-height: 63px; letter-spacing: -4px; }
  .divider { position: absolute; left: 0; top: 0; }
  .side-band {
    position: absolute; left: 0; bottom: 0; width: 100%;
    background: var(--band-soft); color: var(--white); text-align: center;
    font-weight: 700; font-size: 14.5px;
    display: flex; align-items: center; justify-content: center;
  }
  .promo-banner .side-band { height: 36px; }
  .store-banner .side-band { height: 42px; background: rgba(255,255,255,0.12); text-shadow: 0 1px 3px rgba(0,0,0,0.5); }

  .footer-rule { position: absolute; left: 0; top: 587px; width: 1200px; height: 3px; background: var(--ink); }
</style>
</head>
<body>
  <header class="brand">
    <span class="brand-dot"></span>
    <span class="brand-name">Loomhaus Rugs</span>
  </header>

  <section class="banner sale-banner">
    <div class="banner-photo" role="img" aria-label="Bright living room with dark sofa, white armchair, large windows onto greenery and a pastel patchwork carpet"></div>
    <svg class="ribbon" width="80" height="80" viewBox="0 0 80 80">
      <polygon points="0,0 76,0 0,76" fill="var(--ribbon-red)"/>
      <text x="20" y="44" transform="rotate(-45 20 44)" fill="#fff" font-family="Open Sans, Arial, sans-serif" font-weight="800" font-size="13">HUGE</text>
      <text x="27" y="50" transform="rotate(-45 27 50)" fill="#fff" font-family="Lato, Arial, sans-serif" font-weight="700" font-size="7">DISCOUNTS</text>
    </svg>
    <svg class="bracket" width="726" height="399" viewBox="0 0 726 399">
      <polyline points="276,63 294,63 294,220 316,242 294,264 294,294" fill="none" stroke="#fff" stroke-width="2" stroke-dasharray="6 4"/>
    </svg>
    <div class="headline headline-upto">up to</div>
    <div class="headline headline-fifty">50</div>
    <div class="headline headline-percent">%</div>
    <div class="headline headline-off">OFF</div>
    <div class="headline headline-sale">sale</div>
    <div class="headline headline-nowon">now on!</div>
    <div class="offer-band">
      <p class="offer-text">Buy one carpet get<br>extra 50% off</p>
      <span class="shop-button">Shop Now</span>
    </div>
  </section>

  <section class="banner side-banner promo-banner">
    <div class="banner-photo" role="img" aria-label="Modern kitchen with dining table and a deep red vintage carpet"></div>
    <svg class="ribbon" width="62" height="62" viewBox="0 0 62 62">
      <polygon points="0,0 60,0 0,60" fill="var(--ribbon-red)"/>
      <text x="6" y="46" transform="rotate(-45 6 46)" fill="#fff" font-family="Lato, Arial, sans-serif" font-weight="700" font-size="8">PROMOTION</text>
    </svg>
    <div class="side-title promo-title">B2GO</div>
    <svg class="divider" width="354" height="188" viewBox="0 0 354 188">
      <line x1="66" y1="135" x2="182" y2="135" stroke="#fff" stroke-width="1.2" stroke-dasharray="4 3"/>
      <line x1="200" y1="135" x2="318" y2="135" stroke="#fff" stroke-width="1.2" stroke-dasharray="4 3"/>
      <polygon points="191,128 193,133 198,133 194,136 195.5,141 191,138 186.5,141 188,136 184,133 189,133" fill="#fff"/>
    </svg>
    <div class="side-band">Buy Two Carpets, Get One FREE</div>
  </section>

  <section class="banner side-banner store-banner">
    <div class="banner-photo" role="img" aria-label="Spacious lounge with white sofas, fireplace and a dark blue carpet"></div>
    <div class="side-title store-title">NOW<br>OPEN</div>
    <svg class="divider" width="354" height="188" viewBox="0 0 354 188">
      <line x1="92" y1="131" x2="183" y2="131" stroke="#fff" stroke-width="1.2" stroke-dasharray="4 3"/>
      <line x1="201" y1="131" x2="290" y2="131" stroke="#fff" stroke-width="1.2" stroke-dasharray="4 3"/>
      <polygon points="192,124 194,129 199,129 195,132 196.5,137 192,134 187.5,137 189,132 185,129 190,129" fill="#fff"/>
    </svg>
    <div class="side-band">NEW STORE IN BERLIN GERMANY</div>
  </section>

  <div class="footer-rule"></div>
</body>
</html>
```